Redesign Colorful Business Card

Please redesign the card attached. It is too busy. Please don't eliminate any of the words. The repetivite word "free" can be used less often.

Target Market(s)

College Students.

Contact Information for Business Card

The details listed in the attached image

Font styles to use
Sans Serif

Requirements
Must have
• A clear and simple presentation and must be attractive.

```html
<!DOCTYPE html>
<html lang="en">
<head>
<meta charset="UTF-8">
<title>StudyNest Business Card</title>
<link href="https://fonts.googleapis.com/css2?family=Poppins:wght@400;500;600;700&display=swap" rel="stylesheet">
<style>
  :root{
    --scene:#2f3a66;
    --brand-blue:#2443a8;
    --card-light:#bfe3f3;
    --ink-blue:#2443a8;
    --ink-dark:#14224f;
    --tag-red:#e8232a;
    --tag-dark:#a5151a;
    --line-pink:#b0409a;
    --line-green:#6cbf3a;
    --icon-orange:#e0662a;
    --white:#ffffff;
  }
  *{box-sizing:border-box;margin:0;padding:0}
  html,body{width:1200px;height:1200px;overflow:hidden}
  body{background:var(--scene);font-family:"Poppins",sans-serif;position:relative}

  .card{position:absolute;left:180px;width:840px;height:480px;background:var(--card-light);overflow:hidden;box-shadow:0 18px 40px rgba(0,0,0,.35)}
  .card--back{top:80px}
  .card--front{top:630px}

  .brand{position:absolute;display:flex;align-items:center;gap:12px;color:var(--white);font-weight:500;font-size:34px;letter-spacing:.5px}
  .brand__dot{width:34px;height:34px;border-radius:50%;background:var(--card-light)}

  /* back */
  .back__band{position:absolute;left:0;top:0;width:100%;height:250px;background:var(--brand-blue)}
  .card--back .brand{left:50%;top:150px;transform:translateX(-50%)}
  .contacts{position:absolute;left:0;top:290px;width:100%;text-align:center;color:var(--ink-blue);font-size:26px;font-weight:500;letter-spacing:7px;line-height:48px}

  /* front */
  .front__top{position:absolute;left:0;top:0;width:100%;height:64px;background:var(--brand-blue)}
  .front__bottom{position:absolute;left:0;bottom:0;width:100%;height:68px;background:var(--brand-blue);display:flex;align-items:center;justify-content:center;color:var(--white);font-size:17px;letter-spacing:.3px}
  .card--front .brand{left:330px;top:76px;color:var(--brand-blue);font-size:30px}
  .card--front .brand__dot{background:var(--brand-blue);width:28px;height:28px}

  .free-tag{position:absolute;left:34px;top:78px;width:120px;height:120px}
  .free-tag svg{width:100%;height:100%}

  .rule{position:absolute;left:170px;height:3px;width:640px}
  .rule--pink{top:138px;background:var(--line-pink)}
  .rule--green{top:292px;background:var(--line-green)}

  .benefits{position:absolute;left:180px;top:150px;list-style:none}
  .benefit{display:flex;align-items:center;gap:14px;height:46px;color:var(--ink-dark);font-weight:700;font-size:24px;text-transform:uppercase;letter-spacing:-.3px}
  .benefit svg{width:30px;height:30px;flex:none}

  .people-photo{position:absolute;left:420px;top:302px;width:400px;height:110px;background:linear-gradient(90deg,#6b6f78 0%,#e1a54a 35%,#8a6a55 60%,#d9462e 100%);border-radius:4px 4px 0 0}
</style>
</head>
<body>

<section class="card card--back">
  <div class="back__band"></div>
  <div class="brand"><span class="brand__dot"></span><span>StudyNest.com</span></div>
  <div class="contacts">
    <p>W: www.studynest.com</p>
    <p>E: info@studynest.com</p>
    <p>C: 55512 34567</p>
  </div>
</section>

<section class="card card--front">
  <div class="front__top"></div>

  <div class="brand"><span class="brand__dot"></span><span>StudyNest.com</span></div>

  <div class="free-tag">
    <svg viewBox="0 0 120 120" aria-hidden="true">
      <polygon points="20,40 80,0 120,60 60,100" fill="var(--tag-red)"/>
      <polygon points="20,40 10,110 60,100" fill="var(--tag-dark)"/>
      <text x="70" y="62" fill="#fff" font-family="Poppins,sans-serif" font-weight="700" font-size="30" text-anchor="middle" transform="rotate(-34 70 55)">FREE</text>
    </svg>
  </div>

  <div class="rule rule--pink"></div>
  <ul class="benefits">
    <li class="benefit">
      <svg viewBox="0 0 30 30" aria-hidden="true"><circle cx="15" cy="17" r="11" fill="none" stroke="var(--icon-orange)" stroke-width="2.5"/><rect x="12" y="2" width="6" height="3" fill="var(--icon-orange)"/><path d="M15 17V10M15 17l5 3" stroke="var(--icon-orange)" stroke-width="2.5" fill="none"/></svg>
      Cut study time down by up to 50%
    </li>
    <li class="benefit">
      <svg viewBox="0 0 30 30" aria-hidden="true"><rect x="4" y="6" width="22" height="14" rx="1" fill="none" stroke="var(--line-pink)" stroke-width="2.5"/><path d="M1 24h28" stroke="var(--line-pink)" stroke-width="2.5"/></svg>
      Learn a subject without having to go to class
    </li>
    <li class="benefit">
      <svg viewBox="0 0 30 30" aria-hidden="true"><circle cx="15" cy="14" r="10" fill="none" stroke="var(--icon-orange)" stroke-width="2.5"/><path d="M12 24v4h6v-4" stroke="var(--icon-orange)" stroke-width="2.5" fill="none"/></svg>
      Memorize anything quickly
    </li>
  </ul>
  <div class="rule rule--green"></div>

  <div class="people-photo" role="img" aria-label="Photo of stressed students holding their heads"></div>

  <footer class="front__bottom">Copyright Nest Learning Services, LLC 2013-2022 All Rights Reserved</footer>
</section>

</body>
</html>
```